GRA Stationary
GRA, Garnet Resale Advisors
Professional
Dominic T. Harlow
P.O. box 382
Brenwick Hollow, Pa 19507
dtharlow@graadvllc.com
graadvllc.com
I'm open to all ideas. GRA specializes in estate or antique jewelry. So a period approach(Victorian, deco, etc.) might work. But I also like a clean, modern look as well. Color scheme will probably revolve around platinum, but again, I'm open to ideas. Thanks!
needs to have business card, letterhead, fax, and envelope design
logo vector file
KX Press business card format
RGB Color Chart
GRA logo

```html
<!DOCTYPE html>
<html lang="en">
<head>
<meta charset="utf-8">
<title>GRA Stationary – Business Card</title>
<link href="https://fonts.googleapis.com/css2?family=Cormorant+Garamond:wght@500&family=Open+Sans:wght@400;600;700&display=swap" rel="stylesheet">
<style>
  :root {
    --backdrop: #e6e7ea;
    --navy-deep: #061c33;
    --navy: #0b3a63;
    --navy-glow: #1d6aa3;
    --silver-light: #eef0f2;
    --paper: #ffffff;
    --ink: #2a2e33;
    --ink-soft: #5b6068;
    --logo-grey: #8d939b;
    --text-on-dark: #c7d6e6;
  }
  * { margin: 0; padding: 0; box-sizing: border-box; }
  html, body { width: 1200px; height: 874px; overflow: hidden; }
  body {
    background: var(--backdrop);
    font-family: "Open Sans", Arial, sans-serif;
    position: relative;
  }
  .card {
    position: absolute;
    top: 288px;
    width: 520px;
    height: 297px;
    border-radius: 16px;
    overflow: hidden;
    box-shadow: 0 10px 28px rgba(0,0,0,.22);
  }

  /* Front */
  .card-front { left: 50px; }
  .card-front .pattern {
    position: absolute; inset: 0;
    background: radial-gradient(circle at 50% 36%, var(--navy-glow) 0%, var(--navy) 38%, var(--navy-deep) 100%);
  }
  .front-logo {
    position: absolute; left: 0; right: 0; top: 72px;
    text-align: center;
    color: var(--silver-light);
    font-family: "Cormorant Garamond", Georgia, serif;
    font-weight: 500;
  }
  .front-logo .mark { font-size: 50px; letter-spacing: 4px; line-height: 1; }
  .front-logo .company { font-size: 25px; margin-top: 14px; letter-spacing: .5px; }
  .front-url {
    position: absolute; right: 26px; bottom: 40px;
    font-size: 10px; color: var(--text-on-dark); letter-spacing: .3px;
  }

  /* Back */
  .card-back { left: 630px; background: var(--paper); }
  .card-back .pattern {
    position: absolute; inset: 0;
    background: linear-gradient(135deg, #ffffff 0%, #f1f2f4 60%, #e9ebee 100%);
  }
  .card-back svg.swoosh { position: absolute; inset: 0; }
  .back-logo {
    position: absolute; left: 34px; top: 78px;
    display: flex; align-items: baseline; gap: 12px;
    color: var(--logo-grey);
    font-family: "Cormorant Garamond", Georgia, serif;
    font-weight: 500;
  }
  .back-logo .mark { font-size: 34px; letter-spacing: 2px; }
  .back-logo .company { font-size: 19px; }
  .contact {
    position: absolute; left: 360px; top: 52px; width: 140px;
    font-size: 9.5px; line-height: 15.5px; color: var(--ink-soft);
    white-space: nowrap;
  }
  .contact .toll { font-weight: 700; color: var(--ink); }
  .person { position: absolute; left: 34px; top: 198px; }
  .person .name { font-size: 15px; font-weight: 700; color: var(--ink); }
  .person .role { font-size: 10px; color: var(--ink-soft); margin-top: 1px; }
</style>
</head>
<body>

<section class="card card-front" aria-label="Business card front">
  <div class="pattern" role="img" aria-label="Navy background with faint damask pattern"></div>
  <div class="front-logo">
    <div class="mark">GRA</div>
    <div class="company">Garnet Resale Advisors</div>
  </div>
  <div class="front-url">www.graadvllc.com</div>
</section>

<section class="card card-back" aria-label="Business card back">
  <div class="pattern" role="img" aria-label="White background with faint silver damask swirls"></div>
  <svg class="swoosh" width="520" height="297" viewBox="0 0 520 297" aria-hidden="true">
    <defs>
      <linearGradient id="waveBlue" x1="0" y1="0" x2="1" y2="0">
        <stop offset="0" stop-color="#0b3a63"/>
        <stop offset=".6" stop-color="#1b5d93"/>
        <stop offset="1" stop-color="#0b3a63"/>
      </linearGradient>
    </defs>
    <path d="M0,232 C170,268 320,250 420,170 C460,140 495,125 520,120 L520,297 L0,297 Z" fill="#d3d7dc"/>
    <path d="M0,246 C170,280 330,262 430,185 C465,158 495,145 520,140 L520,297 L0,297 Z" fill="#6fa2cc"/>
    <path d="M0,256 C170,288 340,272 440,198 C470,176 498,163 520,158 L520,297 L0,297 Z" fill="url(#waveBlue)"/>
    <path d="M0,268 C180,296 340,284 445,212 C475,192 500,180 520,176" fill="none" stroke="#ffffff" stroke-width="1.4" opacity=".8"/>
    <circle cx="422" cy="108" r="100" fill="#ffffff" stroke="#cfd3d8" stroke-width="6"/>
  </svg>

  <div class="back-logo">
    <span class="mark">GRA</span>
    <span class="company">Garnet Resale Advisors</span>
  </div>

  <div class="contact">
    P.O. box 382<br>
    Brenwick Hollow, Pa 19507<br>
    (888) 555-0148 <span class="toll">Toll Free</span><br>
    (610) 555-0192<br>
    (610) 555-0136<br>
    dtharlow@graadvllc.com<br>
    www.graadvllc.com
  </div>

  <div class="person">
    <div class="name">Dominic T. Harlow</div>
    <div class="role">President</div>
  </div>
</section>

</body>
</html>
```